ebook cover for a womens core fitness business

I need an ebook cover for an email capture gift. The title is "Ways to steady your inner strength". My website provides online workouts for women focussing on their core and pelvic floor muscles. My business is "Stride Well with Dana" I have attached my color scheme as well as logo file

Target Market(s)

Females from child bearing age onwards

Industry/Entity Type

Health And Wellness

Font styles to use
Sans Serif

Colors
33a6d7
0455a3
cee9f5

Requirements
Must have
• Colours as per file.
• Feel fresh and attractive to women but not flowery
• Look professional
Should not have
• Flowers

```html
<!DOCTYPE html>
<html lang="en">
<head>
<meta charset="utf-8">
<title>Ways to steady your inner strength — ebook cover</title>
<link href="https://fonts.googleapis.com/css2?family=Oswald:wght@300;400&display=swap" rel="stylesheet">
<style>
  :root {
    --page-bg: #eef1f3;
    --cover-bg: #f7f7f7;
    --navy: #1b3f6b;
    --brand-blue: #33a6d7;
    --brand-deep: #0455a3;
    --brand-pale: #cee9f5;
    --photo-wall: #d9dcdf;
    --photo-floor: #6f7378;
  }
  * { box-sizing: border-box; margin: 0; padding: 0; }
  html, body {
    width: 1200px;
    height: 1000px;
    overflow: hidden;
    background: var(--page-bg);
  }
  .canvas {
    position: relative;
    width: 1200px;
    height: 1000px;
  }
  .cover {
    position: absolute;
    left: 250px;
    top: 30px;
    width: 700px;
    height: 940px;
    background: var(--cover-bg);
    box-shadow: 0 14px 40px rgba(0,0,0,0.18);
    font-family: "Oswald", "Arial Narrow", sans-serif;
    text-align: center;
  }
  .cover-title {
    position: absolute;
    top: 150px;
    left: 0;
    right: 0;
    text-transform: uppercase;
    line-height: 1;
  }
  .cover-title .lead {
    display: block;
    font-weight: 400;
    font-size: 54px;
    color: var(--navy);
    letter-spacing: -0.5px;
  }
  .cover-title .main {
    display: block;
    margin-top: 10px;
    font-weight: 300;
    font-size: 104px;
    color: var(--brand-blue);
    letter-spacing: 0;
  }
  .photo-row {
    position: absolute;
    top: 460px;
    left: 12px;
    right: 12px;
    display: flex;
    gap: 8px;
  }
  .photo {
    flex: 1;
    height: 320px;
    border: 1px solid #e3e3e3;
  }
  .photo--ball { background: linear-gradient(180deg, #ecebe8 0%, #d8d9da 55%, #9b9ea2 100%); }
  .photo--mat { background: linear-gradient(180deg, #e9e9ea 0%, #c9cbcd 50%, #4d5b78 100%); }
  .photo--ring { background: linear-gradient(180deg, #e4e4e2 0%, #cfd2d4 55%, #5e6a82 100%); }
  .brand {
    position: absolute;
    top: 870px;
    left: 0;
    right: 0;
    font-weight: 400;
    font-size: 30px;
    color: var(--brand-deep);
    letter-spacing: 0.5px;
  }
</style>
</head>
<body>
  <main class="canvas">
    <section class="cover">
      <h1 class="cover-title">
        <span class="lead">Ways to steady your</span>
        <span class="main">Inner strength</span>
      </h1>
      <div class="photo-row">
        <div class="photo photo--ball" role="img" aria-label="Woman seated on an exercise ball pressing light dumbbells overhead"></div>
        <div class="photo photo--mat" role="img" aria-label="Woman on a mat on forearms and one knee, lifting one leg behind"></div>
        <div class="photo photo--ring" role="img" aria-label="Woman kneeling on a mat squeezing a pilates ring in front of her chest"></div>
      </div>
      <p class="brand">Stride Well with Dana</p>
    </section>
  </main>
</body>
</html>
```